Coastal Sentinels Stationery Design Project

I am looking for a suitable stationary design for my company Coastal Sentinels Pty Ltd (ACN 508 214 396).

The requirements can be better explained by visiting my website
"coastal-sentinels.org"

I will be sending letters to Ministers of State and the Heads of Government Agencies so the theme needs to be formal and serious.

A theme with a shield or similar picking on the "guardian" concept would be appropriate

Target Market(s)

Ministers of State and Department Agency Heads and legal firms, the heads of Trustee Companies as well as Members of Coastal Sentinels

Industry/Entity Type

Government

Requirements
Must have
• Letterhead design is a priority - Business Card secondary

Must include tag line "Shielding your savings when the rest walk away" with a registered trade mark superscript at the end that is an R in a circle {Windows Alt +0174 on numeric keypad or Mac Option +R}.

Must include website address "Coastal-Sentinels.org" plus Email address "coastsentinel@fernmail.net

Company name "Coastal Sentinels Pty. Ltd." and Australian Company Number "ACN 508 214 396" needs to be shown more discretely

Address is "47 Brookfern Lane, Marlow Vale, 3281"
Nice to have
• A watermark is something to be considered

```html
<!DOCTYPE html>
<html lang="en">
<head>
<meta charset="utf-8">
<title>Coastal Sentinels Stationery Options</title>
<link href="https://fonts.googleapis.com/css2?family=Arimo:wght@400;700&family=Noto+Sans:wght@400&display=swap" rel="stylesheet">
<style>
  :root {
    --stage: #000000;
    --paper: #ffffff;
    --gold: #d9ad45;
    --royal: #0a14f0;
    --tag-blue: #2b2bd6;
    --ink: #333333;
    --ink-soft: #555555;
    --black-bar: #000000;
    --mark-fade: #f3ecd9;
  }
  * { box-sizing: border-box; margin: 0; padding: 0; }
  html, body { width: 1200px; height: 511px; overflow: hidden; background: var(--stage); }
  body { position: relative; font-family: "Arimo", Arial, sans-serif; }

  .letterhead, .card { position: absolute; background: var(--paper); overflow: hidden; }
  .letterhead { top: 48px; width: 318px; height: 411px; }
  .letterhead--one { left: 51px; }
  .letterhead--two { left: 424px; }

  .brand-dot { position: absolute; border-radius: 50%; }
  .brand-name { position: absolute; color: var(--gold); font-weight: 700; white-space: nowrap; }
  .tagline { position: absolute; white-space: nowrap; }
  .tagline sup { font-size: 0.8em; }

  .letterhead--one .brand-dot { left: 22px; top: 14px; width: 28px; height: 28px; background: var(--royal); }
  .letterhead--one .brand-name { left: 61px; top: 16px; font-size: 12.5px; }
  .letterhead--one .tagline { left: 61px; top: 33px; font-size: 5.8px; color: var(--tag-blue); }

  .letterhead--two .brand-dot { left: 52px; top: 16px; width: 28px; height: 28px; background: var(--black-bar); }
  .letterhead--two .brand-name { left: 93px; top: 19px; font-size: 12.5px; }
  .letterhead--two .tagline { left: 113px; top: 35px; font-size: 5.8px; color: var(--ink); }

  .watermark {
    position: absolute; left: 100px; top: 147px; width: 126px; height: 128px;
    background: radial-gradient(ellipse at center, var(--mark-fade) 0%, rgba(243,236,217,0.5) 55%, rgba(255,255,255,0) 75%);
  }

  .accent-bar { position: absolute; }
  .letterhead .accent-bar--short { left: 0; top: 380px; width: 25px; height: 8px; }
  .letterhead .accent-bar--long { left: 28px; top: 380px; right: 0; height: 8px; background: var(--gold); }
  .accent-bar--blue { background: var(--royal); }
  .accent-bar--black { background: var(--black-bar); }

  .letter-footer {
    position: absolute; left: 80px; top: 391px; display: flex; align-items: center;
    font-size: 4.8px; color: var(--ink-soft); line-height: 1.4;
  }
  .letter-footer .cell { padding: 0 4px; }
  .letter-footer .cell + .cell { border-left: 0.5px solid var(--ink-soft); }
  .letter-footer .address { text-align: right; }
  .contact-line { display: flex; align-items: center; gap: 2px; }
  .contact-line svg { width: 5px; height: 5px; }

  .card { left: 812px; width: 165px; height: 95px; }
  .card--one { top: 178px; }
  .card--two { top: 330px; }
  .card .brand-dot { left: 29px; top: 20px; width: 17px; height: 17px; }
  .card--one .brand-dot { background: var(--royal); }
  .card--two .brand-dot { background: var(--black-bar); }
  .card .brand-name { left: 53px; top: 20px; font-size: 8px; }
  .card .tagline { left: 53px; top: 31px; font-size: 3.3px; color: var(--ink); }
  .card .accent-bar--short { left: 0; top: 54px; width: 9px; height: 8px; }
  .card .accent-bar--long { left: 11px; top: 54px; right: 0; height: 8px; background: var(--gold); }
  .card-details {
    position: absolute; left: 0; right: 0; top: 67px; text-align: center;
    font-size: 4.6px; color: var(--ink-soft); line-height: 8px;
  }
  .card-details .contact-row { display: flex; justify-content: center; gap: 6px; }

  .option-label {
    position: absolute; color: #ffffff; font-family: "Noto Sans", Verdana, sans-serif;
    font-size: 21px; letter-spacing: 1px; transform: translateX(-50%); white-space: nowrap;
  }
</style>
</head>
<body>

<section class="letterhead letterhead--one">
  <span class="brand-dot"></span>
  <div class="brand-name">Coastal Sentinels Pty. Ltd.</div>
  <div class="tagline">Shielding your savings when the rest walk away<sup>®</sup></div>
  <span class="accent-bar accent-bar--short accent-bar--blue"></span>
  <span class="accent-bar accent-bar--long"></span>
  <footer class="letter-footer">
    <div class="cell">ACN 508 214 396</div>
    <div class="cell address">47 Brookfern Lane<br>Marlow Vale, 3281</div>
    <div class="cell">
      <div class="contact-line"><svg viewBox="0 0 10 10"><rect x="1" y="2.5" width="8" height="5.5" fill="none" stroke="#555" stroke-width="1"/><path d="M1 2.5 L5 6 L9 2.5" fill="none" stroke="#555" stroke-width="1"/></svg>coastsentinel@fernmail.net</div>
      <div class="contact-line"><svg viewBox="0 0 10 10"><circle cx="5" cy="5" r="4" fill="#555"/></svg>www.Coastal-Sentinels.org</div>
    </div>
  </footer>
</section>

<section class="letterhead letterhead--two">
  <span class="brand-dot"></span>
  <div class="brand-name">Coastal Sentinels Pty. Ltd.</div>
  <div class="tagline">Shielding your savings when the rest walk away<sup>®</sup></div>
  <div class="watermark" role="img" aria-label="Faint shield emblem watermark"></div>
  <span class="accent-bar accent-bar--short accent-bar--black"></span>
  <span class="accent-bar accent-bar--long"></span>
  <footer class="letter-footer">
    <div class="cell">ACN 508 214 396</div>
    <div class="cell address">47 Brookfern Lane<br>Marlow Vale, 3281</div>
    <div class="cell">
      <div class="contact-line"><svg viewBox="0 0 10 10"><rect x="1" y="2.5" width="8" height="5.5" fill="none" stroke="#555" stroke-width="1"/><path d="M1 2.5 L5 6 L9 2.5" fill="none" stroke="#555" stroke-width="1"/></svg>coastsentinel@fernmail.net</div>
      <div class="contact-line"><svg viewBox="0 0 10 10"><circle cx="5" cy="5" r="4" fill="#555"/></svg>www.Coastal-Sentinels.org</div>
    </div>
  </footer>
</section>

<section class="card card--one">
  <span class="brand-dot"></span>
  <div class="brand-name">Coastal Sentinels</div>
  <div class="tagline">Shielding your savings when the rest walk away<sup>®</sup></div>
  <span class="accent-bar accent-bar--short accent-bar--blue"></span>
  <span class="accent-bar accent-bar--long"></span>
  <div class="card-details">
    <div>47 Brookfern Lane, Marlow Vale, 3281</div>
    <div>ACN 508 214 396</div>
    <div class="contact-row">
      <span class="contact-line"><svg viewBox="0 0 10 10"><rect x="1" y="2.5" width="8" height="5.5" fill="none" stroke="#555" stroke-width="1"/><path d="M1 2.5 L5 6 L9 2.5" fill="none" stroke="#555" stroke-width="1"/></svg>coastsentinel@fernmail.net</span>
      <span class="contact-line"><svg viewBox="0 0 10 10"><circle cx="5" cy="5" r="4" fill="#555"/></svg>www.Coastal-Sentinels.org</span>
    </div>
  </div>
</section>

<section class="card card--two">
  <span class="brand-dot"></span>
  <div class="brand-name">Coastal Sentinels</div>
  <div class="tagline">Shielding your savings when the rest walk away<sup>®</sup></div>
  <span class="accent-bar accent-bar--short accent-bar--black"></span>
  <span class="accent-bar accent-bar--long"></span>
  <div class="card-details">
    <div>47 Brookfern Lane, Marlow Vale, 3281</div>
    <div>ACN 508 214 396</div>
    <div class="contact-row">
      <span class="contact-line"><svg viewBox="0 0 10 10"><rect x="1" y="2.5" width="8" height="5.5" fill="none" stroke="#555" stroke-width="1"/><path d="M1 2.5 L5 6 L9 2.5" fill="none" stroke="#555" stroke-width="1"/></svg>coastsentinel@fernmail.net</span>
      <span class="contact-line"><svg viewBox="0 0 10 10"><circle cx="5" cy="5" r="4" fill="#555"/></svg>www.Coastal-Sentinels.org</span>
    </div>
  </div>
</section>

<div class="option-label" style="left:214px; top:466px;">Option 1</div>
<div class="option-label" style="left:580px; top:466px;">Option 2</div>
<div class="option-label" style="left:903px; top:288px;">Option 1</div>
<div class="option-label" style="left:905px; top:452px;">Option 2</div>

</body>
</html>
```